" O INSTITUTO TERAVUNDA foi idealizado a partir de um ideal de auxílio humanitário a famílias (com algum idoso) com condições de sobrevivência comprometidas devido a problemas de doença, seja ela física; psicológica ou mesmo social. “ Teravunda” significa “dono da coragem” e, apesar de seu principal mantenedor ser uma casa de culto de matriz africana (Dasilore Mitaku Fenjo Arupe),o Centro Cultural visa atender a famílias com idosos que estejam desestruturadas, devido a algum tipo de doença, indiferente a visão política, religiosa e/ou cultural. Acreditamos que o idoso incluído num contexto familiar, ou mesmo num asilo, não deve ser culpado por qualquer atitude de sua juventude. Quem de nós, em idade de produção e escolhas pode garantir estar tomando decisões acertadas para seu futuro? Normalmente são as doenças que comprometem o bem estar social: vícios em bebidas e/ou drogas; doenças patológicas e/ou psicológicas ou mesmo “doenças sociais” desestruturam as relações interpessoais afastando os idosos da realidade. "

```html
<!DOCTYPE html>
<html lang="pt-BR">
<head>
<meta charset="utf-8">
<title>Instituto Teravunda — Blog/Notícias</title>
<link rel="stylesheet" href="https://fonts.googleapis.com/css2?family=Lato:wght@300;400;700;900&display=swap">
<style>
  :root {
    --orange: #e8793a;
    --orange-soft: #f08a50;
    --brown: #4a2a1f;
    --page: #ffffff;
    --backdrop: #ececec;
    --text-muted: #9a9a9a;
    --nav: #e8793a;
    --hero-a: #7d6a4e;
    --hero-b: #a99a82;
    --hero-c: #d9d5cc;
  }
  * { box-sizing: border-box; margin: 0; padding: 0; }
  html, body {
    width: 1200px; height: 1200px; overflow: hidden;
    background: var(--backdrop);
    font-family: "Lato", Arial, sans-serif;
  }
  .site {
    position: absolute; left: 0; top: 175px;
    width: 1200px; height: 850px;
    background: var(--page);
  }
  .site-header {
    height: 100px;
    display: flex; align-items: center;
    padding: 0 40px 0 70px;
  }
  .brand {
    display: flex; align-items: center; gap: 12px;
    color: var(--orange); font-weight: 700; font-size: 24px;
    letter-spacing: 1px;
  }
  .brand-mark {
    width: 30px; height: 30px; border-radius: 50%;
    background: var(--orange);
  }
  .main-nav {
    margin-left: auto;
    display: flex; gap: 22px;
    font-size: 14px; font-weight: 400; color: var(--nav);
  }
  .main-nav .current { font-weight: 700; color: var(--brown); }
  .join-button {
    margin-left: 34px;
    background: var(--brown); color: #fff;
    font-size: 15px; font-weight: 700;
    padding: 10px 20px; border-radius: 3px;
  }
  .social { display: flex; gap: 8px; margin-left: 18px; }
  .social span { width: 14px; height: 14px; background: var(--orange); border-radius: 2px; }
  .hero {
    position: relative; height: 400px;
    background: linear-gradient(100deg, var(--hero-a) 0%, var(--hero-b) 35%, var(--hero-c) 55%, #8c9a7a 80%, #b9b0a0 100%);
  }
  .hero-title {
    position: absolute; left: 95px; top: 210px;
    font-weight: 900; font-size: 40px; line-height: 1.15;
    color: #fff;
  }
  .hero-title .accent { color: var(--orange-soft); display: block; }
  .blog { padding: 55px 0 0 195px; }
  .blog h2 {
    font-weight: 300; font-size: 48px; color: var(--orange);
  }
  .blog p {
    margin-top: 22px; width: 520px;
    font-size: 14px; line-height: 1.6; color: var(--text-muted);
  }
  .thumbs {
    position: absolute; left: 40px; top: 725px;
    display: flex; gap: 25px;
  }
  .thumb { width: 225px; height: 95px; }
  .t1 { background: linear-gradient(120deg, #e7b27a, #c7824d); }
  .t2 { background: linear-gradient(120deg, #6fa0c8, #d6d0c0, #5f8cb5); }
  .t3 { background: linear-gradient(120deg, #7bb5d6, #e8e2d2, #8fb37e); }
  .t4 { background: linear-gradient(120deg, #a7c7e0, #f0d8a0, #5d93c2); }
</style>
</head>
<body>
  <main class="site">
    <header class="site-header">
      <div class="brand"><span class="brand-mark"></span>INSTITUTO TERAVUNDA</div>
      <nav class="main-nav">
        <span>HOME</span>
        <span>QUEM SOMOS</span>
        <span class="current">BLOG/NOTÍCIAS</span>
        <span>GALERIA</span>
        <span>FALE CONOSCO</span>
      </nav>
      <span class="join-button">Associe-se</span>
      <div class="social"><span></span><span></span></div>
    </header>
    <section class="hero" role="img" aria-label="Fotografia de membros do instituto vestidos de branco em atividade ao ar livre">
      <h1 class="hero-title">Fique por dentro de <span class="accent">Nossas Atividades</span></h1>
    </section>
    <section class="blog">
      <h2>Blog/Notícias</h2>
      <p>Acompanhe aqui todas as ações realizadas pelo Instituto, registros das atividades, encontros e eventos com as famílias atendidas e os voluntários que caminham conosco em cada projeto.</p>
    </section>
    <div class="thumbs">
      <div class="thumb t1" role="img" aria-label="Foto de alimentos preparados em evento"></div>
      <div class="thumb t2" role="img" aria-label="Foto de grupo reunido em atividade"></div>
      <div class="thumb t3" role="img" aria-label="Foto de encontro comunitário ao ar livre"></div>
      <div class="thumb t4" role="img" aria-label="Foto de celebração com bandeiras coloridas"></div>
    </div>
  </main>
</body>
</html>
```